TRUCK WASH OUTDOOR DRIVE THROUGH MENU CONTEST

WE NEED A DRIVE THROUGH MENU WITH OUR SERVICES AND PRICES. I HAVE ATTACHED A FEW EXAMPLES THAT I STARTED.

I WANT THIS TO BE EYE CATCHING WITH BRIGHT COLORS

Target Market(s)

TRUCK WASH AND DETAIL SHOP, TRANSPORTATION.

Requirements
Must have
• INCORPORATE MY LOGO INTO THE SIGN.
• FINAL PROJECT MUST BE IN .AI FORMAT.
• COMPANY COLORS ARE RED AND BLUE

```html
<!DOCTYPE html>
<html lang="en">
<head>
<meta charset="utf-8">
<title>Highway Suds – Drive Through Menu</title>
<link href="https://fonts.googleapis.com/css2?family=Michroma&family=Russo+One&display=swap" rel="stylesheet">
<style>
  :root {
    --bg: #f2f2f2;
    --ink: #111111;
    --price: #e8202a;
    --brand-red: #e8202a;
    --brand-blue: #2aa3de;
    --express: #1f9a44;
    --platinum: #7a4fa0;
    --silver: #6b6b6b;
    --gold: #8a5a30;
  }
  * { margin: 0; padding: 0; box-sizing: border-box; }
  html, body { width: 1200px; height: 830px; overflow: hidden; background: var(--bg); }
  .menu { position: relative; width: 1200px; height: 830px; background: var(--bg); font-family: "Michroma", sans-serif; }
  .drops { position: absolute; inset: 0; }
  .menu-title {
    position: absolute; top: 22px; left: 0; width: 100%; text-align: center;
    font-size: 29px; color: var(--ink); letter-spacing: 0.5px; line-height: 1;
  }
  .item {
    position: absolute; white-space: nowrap; font-size: 18px; line-height: 1;
    transform: translate(-50%, -50%) rotate(var(--r, 0deg));
  }
  .express .item { color: var(--express); }
  .platinum .item { color: var(--platinum); }
  .silver .item { color: var(--silver); }
  .gold .item { color: var(--gold); }
  .tier-badge { position: absolute; transform: translate(-50%, -50%); text-align: center; }
  .tier-price { font-size: 27px; color: var(--price); display: block; }
  .tier-name { font-family: "Russo One", sans-serif; font-size: 32px; display: block; margin-top: 6px; }
  .express .tier-name { color: var(--express); }
  .platinum .tier-name { color: var(--platinum); }
  .silver .tier-name { color: var(--silver); }
  .gold .tier-name { color: var(--gold); }
  .brand {
    position: absolute; left: 600px; top: 470px; transform: translate(-50%, -50%);
    display: flex; flex-direction: column; align-items: center; gap: 14px;
  }
  .brand-dot { width: 30px; height: 30px; border-radius: 50%; background: var(--brand-blue); }
  .brand-name {
    font-family: "Russo One", sans-serif; font-size: 46px; color: var(--brand-red);
    line-height: 1.05; text-align: center;
  }
  .footer-note {
    position: absolute; top: 742px; left: 0; width: 100%; text-align: center;
    font-size: 21px; line-height: 34px; color: var(--ink);
  }
</style>
</head>
<body>
<main class="menu">
  <svg class="drops" width="1200" height="830" viewBox="0 0 1200 830" aria-hidden="true">
    <defs>
      <radialGradient id="drop-fill" cx="45%" cy="40%" r="65%">
        <stop offset="0%" stop-color="#ffffff"/>
        <stop offset="55%" stop-color="#cfe5f3"/>
        <stop offset="85%" stop-color="#8fbedc"/>
        <stop offset="100%" stop-color="#4f8db5"/>
      </radialGradient>
      <radialGradient id="drop-shadow" cx="50%" cy="50%" r="50%">
        <stop offset="0%" stop-color="#9fb4c4" stop-opacity="0.55"/>
        <stop offset="100%" stop-color="#9fb4c4" stop-opacity="0"/>
      </radialGradient>
    </defs>
    <ellipse cx="300" cy="290" rx="150" ry="90" fill="url(#drop-shadow)"/>
    <ellipse cx="845" cy="300" rx="150" ry="90" fill="url(#drop-shadow)"/>
    <ellipse cx="380" cy="650" rx="160" ry="90" fill="url(#drop-shadow)"/>
    <ellipse cx="860" cy="675" rx="150" ry="90" fill="url(#drop-shadow)"/>

    <ellipse cx="286" cy="196" rx="104" ry="86" fill="url(#drop-fill)"/>
    <ellipse cx="830" cy="208" rx="108" ry="92" fill="url(#drop-fill)"/>
    <ellipse cx="370" cy="556" rx="122" ry="100" fill="url(#drop-fill)"/>
    <ellipse cx="852" cy="578" rx="106" ry="104" fill="url(#drop-fill)"/>

    <g fill="url(#drop-fill)">
      <circle cx="640" cy="76" r="9"/><circle cx="571" cy="118" r="9"/>
      <circle cx="597" cy="168" r="8"/><circle cx="413" cy="155" r="9"/>
      <circle cx="447" cy="192" r="13"/><circle cx="488" cy="202" r="11"/>
      <circle cx="728" cy="162" r="9"/><circle cx="706" cy="200" r="7"/>
      <circle cx="680" cy="214" r="10"/><circle cx="497" cy="257" r="5"/>
      <circle cx="490" cy="392" r="6"/><circle cx="705" cy="395" r="6"/>
      <circle cx="760" cy="410" r="11"/><circle cx="477" cy="430" r="11"/>
      <circle cx="418" cy="448" r="10"/><circle cx="819" cy="446" r="11"/>
      <circle cx="615" cy="570" r="9"/><circle cx="692" cy="609" r="16"/>
      <circle cx="790" cy="120" r="4"/>
    </g>
  </svg>

  <h1 class="menu-title">STANDARD TRACTOR &amp; TRAILER (53’)</h1>

  <section class="tier express">
    <div class="tier-badge" style="left:286px; top:196px;">
      <span class="tier-price">$50.00</span><span class="tier-name">EXPRESS</span>
    </div>
    <span class="item" style="left:108px; top:137px; --r:20deg;">PRE-SOAK</span>
    <span class="item" style="left:122px; top:196px;">SOAP</span>
    <span class="item" style="left:132px; top:257px; --r:-20deg;">RINSE</span>
  </section>

  <section class="tier platinum">
    <div class="tier-badge" style="left:830px; top:222px;">
      <span class="tier-price">$200.00</span><span class="tier-name">PLATINUM</span>
    </div>
    <span class="item" style="left:990px; top:86px; --r:-30deg;">PRE-SOAK</span>
    <span class="item" style="left:1062px; top:120px; --r:-20deg;">SOAP &amp; SCRUB</span>
    <span class="item" style="left:1010px; top:197px;">RINSE</span>
    <span class="item" style="left:1044px; top:264px; --r:15deg;">TIRE SHINE</span>
    <span class="item" style="left:1048px; top:364px; --r:38deg;">PLATINUM PROTECT</span>
  </section>

  <section class="tier silver">
    <div class="tier-badge" style="left:363px; top:568px;">
      <span class="tier-price">$100.00</span><span class="tier-name">SILVER</span>
    </div>
    <span class="item" style="left:162px; top:507px; --r:20deg;">PRE-SOAK</span>
    <span class="item" style="left:128px; top:570px;">SOAP &amp; SCRUB</span>
    <span class="item" style="left:198px; top:624px; --r:-16deg;">RINSE</span>
    <span class="item" style="left:198px; top:689px; --r:-33deg;">TIRE SHINE</span>
  </section>

  <section class="tier gold">
    <div class="tier-badge" style="left:850px; top:610px;">
      <span class="tier-price">$150.00</span><span class="tier-name">GOLD</span>
    </div>
    <span class="item" style="left:1018px; top:486px; --r:-30deg;">PRE-SOAK</span>
    <span class="item" style="left:1062px; top:526px; --r:-22deg;">SOAP &amp; SCRUB</span>
    <span class="item" style="left:1010px; top:600px;">RINSE</span>
    <span class="item" style="left:1042px; top:654px; --r:15deg;">TIRE SHINE</span>
    <span class="item" style="left:1042px; top:724px; --r:33deg;">WET X POLISH</span>
  </section>

  <div class="brand">
    <span class="brand-dot"></span>
    <span class="brand-name">HIGHWAY<br>SUDS</span>
  </div>

  <p class="footer-note">FOR MORE OPTIONS<br>PLEASE ASK FRONT DESK</p>
</main>
</body>
</html>
```